Website for "Bright Over Dusk Ltd" cleaning bsuiness

We require a website to expose our business to the local market. We want to provide background on who we are and what we do but in an easily digestible way. We clean domestic and commercial premises and want to provide a list of all of our services to potential customers. We operate out of Warrington in the UK.

We would like the website to be animated in some way so that the experience of using it is not dull or mundane. This website needs to be an extension of our company.

Target Market(s)

30 - 60 year olds for Domestic plus commercial clients

Industry/Entity Type

Cleaning Service

Coding

Coded - Design and coding required

Number of Pages Required

4 page

Font styles to use
Sans Serif

Colors
0455a3
3176b5
85acd3
cfdeed
ffffff
000000
1b1b1b
c8c8c8
757575

Requirements
Must have
• Logo which has been provided. Theme based around the logo and its colours. Simple layout to avoid confusion.
Nice to have
• Animations where possible to impress the customer.
Should not have
• any pictures of cleaning equipment, fairies, maids etc

```html
<!DOCTYPE html>
<html lang="en">
<head>
<meta charset="utf-8">
<title>Bright Over Dusk Ltd — Professional Cleaning Service</title>
<link href="https://fonts.googleapis.com/css2?family=Roboto:wght@300;400;500;700&family=Dancing+Script:wght@500&display=swap" rel="stylesheet">
<style>
:root{
  --primary:#0455a3;
  --link:#3176b5;
  --soft:#85acd3;
  --pale:#cfdeed;
  --white:#ffffff;
  --black:#000000;
  --ink:#1b1b1b;
  --rule:#c8c8c8;
  --muted:#757575;
  --navy:#14238a;
  --footer:#2b2f36;
}
*{box-sizing:border-box;margin:0;padding:0}
html,body{width:1200px;height:4045px;overflow:hidden;background:var(--white)}
body{font-family:'Roboto',sans-serif;color:var(--ink);position:relative}
.page{position:relative;width:1200px;height:4045px;overflow:hidden}
.abs{position:absolute}
.script{font-family:'Dancing Script',cursive;color:var(--navy);font-size:19px}
.small{font-size:12.5px;line-height:1.6;color:var(--muted)}

/* header */
.header{top:0;left:0;width:1200px;height:72px;background:var(--white);z-index:5}
.nav{right:40px;top:26px;display:flex;gap:34px;font-size:16px;color:var(--ink)}
.nav a{color:var(--ink);text-decoration:none}
.nav a.active{color:var(--primary)}
.brand{left:30px;top:0;width:300px;height:170px;background:var(--white);border-radius:0 0 150px 150px;z-index:6;display:flex;align-items:center;justify-content:center;gap:10px}
.brand .dot{width:22px;height:22px;border-radius:50%;background:var(--primary)}
.brand .name{font-weight:700;font-size:21px;color:var(--primary)}

/* hero */
.hero{top:72px;left:0;width:1200px;height:575px;background:linear-gradient(100deg,#2a1d14 0%,#4a3423 40%,#6b5136 70%,#3b2b1f 100%)}
.hero-photo{right:60px;top:0;width:420px;height:575px;background:linear-gradient(180deg,#c99a83 0%,#d44f5f 55%,#3a2a21 100%);opacity:.75}
.hero h1{left:80px;top:205px;font-size:46px;font-weight:400;color:var(--white)}
.hero .script{left:82px;top:268px;color:var(--soft);font-size:22px}
.hero p{left:80px;top:310px;width:520px;font-size:13px;line-height:1.6;color:#e8e2dc}
.btn{left:80px;top:400px;width:180px;height:46px;background:var(--link);color:var(--white);font-size:15px;display:flex;align-items:center;justify-content:center;border-radius:3px}

/* shared headings */
.sec-title{left:0;width:1200px;text-align:center;font-size:27px;font-weight:400;color:var(--navy)}
.sec-sub{left:0;width:1200px;text-align:center}
.divider{left:540px;width:120px;height:20px}

/* services diagram */
.intro{left:255px;top:830px;width:690px;text-align:center}
.diagram{left:0;top:940px;width:1200px;height:560px}
.hub{left:490px;top:1084px;width:190px;height:190px;border-radius:50%;border:6px solid var(--navy);background:var(--white);display:flex;flex-direction:column;align-items:center;justify-content:center;gap:8px;text-align:center}
.hub .dot{width:16px;height:16px;border-radius:50%;background:var(--primary)}
.hub .name{font-weight:700;font-size:18px;line-height:1.2;color:var(--primary);width:140px}
.node{width:92px;height:92px;border-radius:50%;border:4px solid var(--pale);box-shadow:0 0 0 1px var(--rule)}
.num{width:36px;height:36px;border-radius:50%;background:var(--ink);color:var(--white);border:3px solid var(--white);font-size:15px;display:flex;align-items:center;justify-content:center}
.svc{width:280px}
.svc h3{font-size:19px;font-weight:400;color:var(--link);margin-bottom:6px}
.svc.right{text-align:right}

/* about band */
.about-bg{left:0;top:1537px;width:1200px;height:660px}
.about-photo{left:13px;top:1524px;width:257px;height:690px;background:linear-gradient(180deg,#e7e1da 0%,#f3f3f3 40%,#3d8fd6 70%,#f0c23a 100%)}
.about h2{left:526px;top:1676px;font-size:35px;font-weight:400;color:var(--navy)}
.about .script{left:528px;top:1722px;font-size:16px}
.about .lead{left:526px;top:1770px;width:640px}
.col h4{font-size:19px;font-weight:400;color:var(--ink);margin-bottom:10px}
.col .small{margin-bottom:8px}
.col .more{font-size:13px;color:var(--primary)}

/* why choose us */
.why{top:2400px;display:flex;left:0;width:1200px}
.why-item{position:absolute;width:200px;text-align:center}
.why-item .shape{width:110px;height:110px;margin:0 auto;transform:rotate(45deg);border-radius:6px;box-shadow:0 6px 10px rgba(0,0,0,.15)}
.why-item .label{margin-top:34px;font-size:17px;color:var(--ink)}

/* testimonial */
.test-bg{left:0;top:2610px;width:1200px;height:640px}
.test-man{left:728px;top:2576px;width:472px;height:650px;background:linear-gradient(180deg,#f2ece4 0%,#b9cfe5 45%,#86a6c7 75%,#51606e 100%)}
.test-sofa{left:65px;top:2990px;width:830px;height:195px;background:linear-gradient(180deg,#eae2c4 0%,#c5c98a 55%,#9fa76a 100%)}
.test h2{left:80px;top:2712px;font-size:40px;font-weight:400;color:var(--navy)}
.test .arrows{left:310px;top:2722px;font-size:30px;color:var(--ink);letter-spacing:14px}
.test .script{left:82px;top:2762px;font-size:16px}
.quote-open{left:75px;top:2810px;font-size:90px;line-height:1;color:var(--primary);font-family:Georgia,serif}
.quote-close{left:350px;top:2900px;font-size:90px;line-height:1;color:var(--primary);font-family:Georgia,serif}
.test .body{left:148px;top:2830px;width:600px;font-size:14px;line-height:1.6;color:var(--ink)}
.test .who{left:148px;top:2960px;font-size:14px;color:var(--link)}
.test .role{left:148px;top:2984px;font-size:14px;color:var(--ink)}

/* trust */
.step{width:330px;display:flex;gap:18px}
.step .icon{flex:none;width:82px;height:82px;border-radius:50%;background:var(--navy);display:flex;align-items:center;justify-content:center}
.step h3{font-size:19px;font-weight:400;color:var(--link);margin:4px 0 8px}
.step .small{width:220px}

/* footer */
.footer{left:0;top:3614px;width:1200px;height:399px;background:linear-gradient(180deg,#3a3d42 0%,#2b2f36 60%,#23262b 100%)}
.fcol h4{font-size:19px;font-weight:400;color:var(--soft);padding-bottom:10px;border-bottom:1px solid #55595f;margin-bottom:14px}
.fcol ul{list-style:none}
.fcol li{font-size:13.5px;color:var(--white);line-height:27px}
.fcol li::before{content:"›";margin-right:8px;color:var(--rule)}
.crow{display:flex;gap:10px;color:var(--white);font-size:13px;line-height:1.6;margin-bottom:10px}
.crow .free{color:var(--soft);font-size:16px}
.news p{font-size:12px;color:var(--white);line-height:1.6;margin-bottom:10px}
.news .field{width:200px;height:26px;background:var(--white);font-size:11px;color:var(--muted);padding:6px 8px;margin-bottom:8px}
.news .go{width:76px;height:22px;background:var(--primary);color:var(--white);font-size:11px;display:flex;align-items:center;justify-content:center}
.social li{display:flex;align-items:center;gap:10px;font-size:13px;color:var(--white);line-height:36px}
.social li::before{content:none}
.social .sq{width:24px;height:24px;border-radius:3px;background:var(--link)}
.copyright{left:0;top:4013px;width:1200px;height:32px;background:var(--link);color:var(--white);font-size:12px;text-align:center;line-height:32px}
</style>
</head>
<body>
<div class="page">

  <!-- header -->
  <header class="abs header">
    <nav class="abs nav">
      <a class="active">Home</a><a>About Us</a><a>Our Services</a><a>Why Choose Us</a><a>Book A Cleaner</a><a>Contacts</a>
    </nav>
  </header>
  <div class="abs brand"><span class="dot"></span><span class="name">Bright Over Dusk Ltd</span></div>

  <!-- hero -->
  <section class="abs hero" role="img" aria-label="Softly lit living room interior">
    <div class="abs hero-photo" role="img" aria-label="Smiling cleaner in red gloves wiping a window"></div>
  </section>
  <div class="hero">
    <h1 class="abs" style="left:80px;top:277px;font-size:46px;font-weight:400;color:#fff">We Make Your Home Clean.</h1>
    <div class="abs script" style="left:82px;top:340px;color:var(--soft);font-size:22px">Experience The Difference</div>
    <p class="abs" style="left:80px;top:382px;width:520px;font-size:13px;line-height:1.6;color:#e8e2dc">Lorem ipsum dolor sit amet, consectetur adipiscing elit. Quisque sit amet nisl et arcu blandit posuere. Praesent egestas ultrices dolor, ac rutrum lorem mollis commodo. Vivamus semper rhoncus sapien, vitae condimentum dui cursus sit amet.</p>
    <div class="abs btn" style="top:472px">Contact Us</div>
  </div>

  <!-- welcome / services -->
  <h2 class="abs sec-title" style="top:700px">Welcome To Bright Over Dusk Ltd</h2>
  <div class="abs sec-sub script" style="top:740px;font-size:16px">Professional Cleaning Service</div>
  <svg class="abs divider" style="top:775px" viewBox="0 0 120 20"><line x1="0" y1="10" x2="48" y2="10" stroke="#c8c8c8"/><line x1="72" y1="10" x2="120" y2="10" stroke="#c8c8c8"/><path d="M60 0 L62 8 L70 10 L62 12 L60 20 L58 12 L50 10 L58 8Z" fill="#14238a"/></svg>
  <p class="abs intro small">Lorem ipsum dolor sit amet, consectetur adipiscing elit. Praesent tristique odio ac gravida lobortis. Phasellus euismod, quis mollis egestas, eros eros egestas orci, at blandit ex sem in neque. In dictum dictum libero, in semper magna pretium fringilla. Mauris non massa cursus, vehicula eros quis, fringilla magna.</p>

  <svg class="abs" style="left:0;top:0" width="1200" height="1600" aria-hidden="true">
    <g stroke="#14238a" stroke-width="2">
      <line x1="585" y1="1179" x2="696" y2="998"/>
      <line x1="585" y1="1179" x2="823" y2="1154"/>
      <line x1="585" y1="1179" x2="782" y2="1322"/>
      <line x1="585" y1="1179" x2="639" y2="1421"/>
      <line x1="585" y1="1179" x2="431" y2="1340"/>
      <line x1="585" y1="1179" x2="369" y2="1146"/>
      <line x1="585" y1="1179" x2="507" y2="992"/>
    </g>
  </svg>
  <div class="abs hub"><span class="dot"></span><span class="name">Bright Over Dusk Ltd</span></div>

  <div class="abs node" style="left:650px;top:952px;background:linear-gradient(135deg,#c9a27d,#f1ece6)" role="img" aria-label="Domestic cleaning scene"></div>
  <div class="abs node" style="left:777px;top:1108px;background:linear-gradient(135deg,#d9e4ee,#4c5a66)" role="img" aria-label="Carpet being vacuumed"></div>
  <div class="abs node" style="left:736px;top:1276px;background:linear-gradient(135deg,#e9dfd6,#3aa3b5)" role="img" aria-label="Ironing clothes"></div>
  <div class="abs node" style="left:593px;top:1375px;background:linear-gradient(135deg,#bfc6cc,#3b4a55)" role="img" aria-label="Tiled floor steam cleaning"></div>
  <div class="abs node" style="left:385px;top:1294px;background:linear-gradient(135deg,#e6f2fa,#4aa3d8)" role="img" aria-label="Toilet cleaning"></div>
  <div class="abs node" style="left:323px;top:1100px;background:linear-gradient(135deg,#f0ede8,#2c8fd0)" role="img" aria-label="Desk polishing"></div>
  <div class="abs node" style="left:461px;top:946px;background:linear-gradient(135deg,#6d7a8a,#1f2c3f)" role="img" aria-label="Commercial office cleaning"></div>

  <div class="abs num" style="left:714px;top:952px">1</div>
  <div class="abs num" style="left:840px;top:1135px">2</div>
  <div class="abs num" style="left:790px;top:1336px">3</div>
  <div class="abs num" style="left:610px;top:1452px">4</div>
  <div class="abs num" style="left:370px;top:1348px">5</div>
  <div class="abs num" style="left:311px;top:1128px">6</div>
  <div class="abs num" style="left:446px;top:952px">7</div>

  <div class="abs svc" style="left:769px;top:958px"><h3>Domestic Services</h3><p class="small">Lorem ipsum dolor sit amet, consectetur adipiscing elit. Aenean id iaculis eros.</p></div>
  <div class="abs svc" style="left:903px;top:1138px"><h3>Carpet Cleaning</h3><p class="small">Lorem ipsum dolor sit amet, consectetur adipiscing elit. Aenean id iaculis eros.</p></div>
  <div class="abs svc" style="left:855px;top:1338px"><h3>Ironing</h3><p class="small">Lorem ipsum dolor sit amet, consectetur adipiscing elit. Aenean id iaculis eros.</p></div>
  <div class="abs svc" style="left:677px;top:1462px"><h3>Tiled floor steam clean</h3><p class="small">Lorem ipsum dolor sit amet, consectetur adipiscing elit. Aenean id iaculis eros.</p></div>
  <div class="abs svc right" style="left:71px;top:1352px"><h3>Toilet cleaning</h3><p class="small">Lorem ipsum dolor sit amet, consectetur adipiscing elit. Aenean id iaculis eros.</p></div>
  <div class="abs svc right" style="left:17px;top:1130px"><h3>Desk polishing</h3><p class="small">Lorem ipsum dolor sit amet, consectetur adipiscing elit. Aenean id iaculis eros.</p></div>
  <div class="abs svc right" style="left:151px;top:958px"><h3>Commercial Services</h3><p class="small">Lorem ipsum dolor sit amet, consectetur adipiscing elit. Aenean id iaculis eros.</p></div>

  <!-- about band -->
  <svg class="abs about-bg" viewBox="0 0 1200 660" preserveAspectRatio="none" role="img" aria-label="Faded bright room interior">
    <defs><linearGradient id="aboutFill" x1="0" y1="0" x2="1" y2="1"><stop offset="0" stop-color="#f4f5f7"/><stop offset="1" stop-color="#dfe3e8"/></linearGradient></defs>
    <polygon points="0,110 1200,0 1200,560 0,660" fill="url(#aboutFill)"/>
  </svg>
  <div class="abs about-photo" role="img" aria-label="Cleaner in white overalls beside a cart"></div>
  <div class="about">
    <h2 class="abs">One Of The Best Company In UK</h2>
    <div class="abs script">We Clean Domestic And Commercial Premises</div>
    <p class="abs lead small">Lorem ipsum dolor sit amet, consectetur adipiscing elit. Praesent tristique odio ac gravida lobortis. Phasellus euismod, quis mollis egestas, eros eros egestas orci, at blandit ex sem in neque. In dictum dictum libero, in semper magna pretium fringilla.</p>
    <div class="abs col" style="left:526px;top:1856px;width:300px"><h4>Company History</h4><p class="small">Lorem ipsum dolor sit amet, consectetur adipiscing elit. Praesent tristique odio ac gravida lobortis. Phasellus euismod, quis mollis egestas, eros eros egestas orci, at blandit ex sem in neque. Nam blandit feugiat orci.</p><span class="more">Read More...</span></div>
    <div class="abs col" style="left:850px;top:1856px;width:300px"><h4>Our Philosophy</h4><p class="small">Lorem ipsum dolor sit amet, consectetur adipiscing elit. Praesent tristique odio ac gravida lobortis. Phasellus euismod, quis mollis egestas, eros eros egestas orci, at blandit ex sem in neque. Nam blandit feugiat orci.</p><span class="more">Read More...</span></div>
  </div>

  <!-- why choose us -->
  <h2 class="abs sec-title" style="top:2212px">Why Choose Us</h2>
  <div class="abs sec-sub script" style="top:2248px;font-size:16px">Our Qualities Make Us Different</div>
  <svg class="abs divider" style="top:2284px" viewBox="0 0 120 20"><line x1="0" y1="10" x2="48" y2="10" stroke="#c8c8c8"/><line x1="72" y1="10" x2="120" y2="10" stroke="#c8c8c8"/><path d="M60 0 L62 8 L70 10 L62 12 L60 20 L58 12 L50 10 L58 8Z" fill="#14238a"/></svg>
  <div class="abs why-item" style="left:54px;top:2386px"><div class="shape" style="background:linear-gradient(135deg,#e9eef4,#2f7fc8)" role="img" aria-label="Team of expert cleaners"></div><div class="label">Expert Cleaners</div></div>
  <div class="abs why-item" style="left:272px;top:2386px"><div class="shape" style="background:linear-gradient(135deg,#f1f1f1,#c0262d)" role="img" aria-label="Price tag"></div><div class="label">Affordable Price</div></div>
  <div class="abs why-item" style="left:493px;top:2386px"><div class="shape" style="background:linear-gradient(135deg,#cfdeed,#3d4f63)" role="img" aria-label="Cleaner at work"></div><div class="label">Regular Cleaning</div></div>
  <div class="abs why-item" style="left:714px;top:2386px"><div class="shape" style="background:linear-gradient(135deg,#f5f5f5,#6c7480)" role="img" aria-label="Hands typing on a laptop"></div><div class="label">Easy Online Booking</div></div>
  <div class="abs why-item" style="left:933px;top:2386px"><div class="shape" style="background:linear-gradient(135deg,#fff7d6,#e8b62a)" role="img" aria-label="Satisfaction guarantee seal"></div><div class="label">100% Satisfaction</div></div>

  <!-- testimonial -->
  <svg class="abs test-bg" viewBox="0 0 1200 640" preserveAspectRatio="none" aria-hidden="true">
    <polygon points="0,0 1200,110 1200,640 0,560" fill="#ece6d8"/>
  </svg>
  <div class="abs test-sofa" role="img" aria-label="Light green sofa in a bright lounge"></div>
  <div class="abs test-man" role="img" aria-label="Smiling customer in a light blue shirt"></div>
  <div class="test">
    <h2 class="abs">Testimonial</h2>
    <div class="abs arrows">‹›</div>
    <div class="abs script">What Others Say</div>
    <div class="abs quote-open">“</div>
    <p class="abs body">Vivamus porttitor augue mauris, quis commodo sapien imperdiet vel. Maecenas fermentum purus convallis magna consequat vehicula. Aenean mollis mi eu nunc consequat efficitur. Suspendisse ut euismod sem. Morbi eget arcu imperdiet, semper nunc pharetra, congue ipsum. Quisque quis est in leo pharetra scelerisque nec eget metus. Cras felis sapien, posuere ut lorem quis, congue congue ex.</p>
    <div class="abs quote-close">”</div>
    <div class="abs who">Alan Carter</div>
    <div class="abs role">Customer</div>
  </div>

  <!-- trust -->
  <h2 class="abs sec-title" style="top:3280px">Your Trust &amp; Security Is Our Priority</h2>
  <div class="abs sec-sub script" style="top:3318px;font-size:16px">Book Now</div>
  <svg class="abs divider" style="top:3356px" viewBox="0 0 120 20"><line x1="0" y1="10" x2="48" y2="10" stroke="#c8c8c8"/><line x1="72" y1="10" x2="120" y2="10" stroke="#c8c8c8"/><path d="M60 0 L62 8 L70 10 L62 12 L60 20 L58 12 L50 10 L58 8Z" fill="#14238a"/></svg>

  <div class="abs step" style="left:80px;top:3436px">
    <div class="icon"><svg width="40" height="40" viewBox="0 0 40 40"><rect x="6" y="8" width="28" height="26" rx="2" fill="none" stroke="#fff" stroke-width="2.5"/><line x1="6" y1="15" x2="34" y2="15" stroke="#fff" stroke-width="2.5"/><line x1="13" y1="4" x2="13" y2="11" stroke="#fff" stroke-width="2.5"/><line x1="27" y1="4" x2="27" y2="11" stroke="#fff" stroke-width="2.5"/></svg></div>
    <div><h3>Book</h3><p class="small">Curabitur ornare sem tellus, a varius dolor aliquam et. Aenean volutpat, diam et ele mentum sollicitudin.</p></div>
  </div>
  <div class="abs step" style="left:439px;top:3436px">
    <div class="icon"><svg width="40" height="40" viewBox="0 0 40 40"><path d="M9 21 L17 29 L32 12" fill="none" stroke="#fff" stroke-width="4" stroke-linecap="round" stroke-linejoin="round"/></svg></div>
    <div><h3>Confirm</h3><p class="small">Curabitur ornare sem tellus, a varius dolor aliquam et. Aenean volutpat, diam et ele mentum sollicitudin.</p></div>
  </div>
  <div class="abs step" style="left:795px;top:3436px">
    <div class="icon"><svg width="40" height="40" viewBox="0 0 40 40"><path d="M20 5 C20 5 9 18 9 25 a11 11 0 0 0 22 0 C31 18 20 5 20 5Z" fill="none" stroke="#fff" stroke-width="2.5"/></svg></div>
    <div><h3>Clean</h3><p class="small">Curabitur ornare sem tellus, a varius dolor aliquam et. Aenean volutpat, diam et ele mentum sollicitudin.</p></div>
  </div>

  <!-- footer -->
  <footer class="abs footer">
    <div class="abs fcol" style="left:80px;top:66px;width:190px">
      <h4>Quick Links</h4>
      <ul><li>Home</li><li>About Us</li><li>Our Services</li><li>Why Choose Us</li><li>Book A Cleaner</li><li>Become A Cleaner</li><li>Contact Us</li></ul>
    </div>
    <div class="abs fcol" style="left:302px;top:66px;width:290px">
      <h4>Contact Information</h4>
      <div class="crow"><svg width="14" height="18" viewBox="0 0 14 18" style="flex:none;margin-top:3px"><path d="M7 1a6 6 0 0 0-6 6c0 4.5 6 10 6 10s6-5.5 6-10a6 6 0 0 0-6-6z" fill="#fff"/><circle cx="7" cy="7" r="2.2" fill="#2b2f36"/></svg><span>Unit 12 Head Office, 4 Linden Court Drive, Riverside Park, Warrington WA1 4RT PO Box 2210 Warrington WA1 9ZZ</span></div>
      <div class="crow"><svg width="14" height="18" viewBox="0 0 14 18" style="flex:none"><rect x="2" y="1" width="10" height="16" rx="2" fill="none" stroke="#fff" stroke-width="1.6"/><circle cx="7" cy="14" r="1" fill="#fff"/></svg><span class="free">Freecall 0800 555 0192</span></div>
      <div class="crow"><svg width="16" height="14" viewBox="0 0 16 14" style="flex:none;margin-top:3px"><rect x="1" y="2" width="14" height="10" fill="none" stroke="#fff" stroke-width="1.5"/><path d="M1 2 L8 8 L15 2" fill="none" stroke="#fff" stroke-width="1.5"/></svg><span>info@brightoverdusk.co.uk</span></div>
    </div>
    <div class="abs fcol news" style="left:639px;top:66px;width:230px">
      <h4>Newsletter Signup</h4>
      <p>Please enter your email address below to receive our FREE newsletter</p>
      <div class="field">Your Email ID</div>
      <div class="go">Subscribe</div>
    </div>
    <div class="abs fcol social" style="left:933px;top:66px;width:190px">
      <h4>Follow Us</h4>
      <ul><li><span class="sq"></span>Chatterbox</li><li><span class="sq"></span>WorkLink</li><li><span class="sq"></span>Chirper</li><li><span class="sq"></span>Email</li></ul>
    </div>
  </footer>
  <div class="abs copyright">Copyright © Bright Over Dusk Ltd . All Rights Are Reserved.</div>

</div>
</body>
</html>
```